Cybersecurity company is looking for business card.

I need a business card design for our company, we are a cybersecurity company providing advance technology to protect agains any kind of malware. We need a fresh modern design it should communicate modern, technology and growth.

Target Market(s)

Business to business

Industry/Entity Type

Business

Contact Information for Business Card

Should have location, address, fax, mobile, phone, email and website.

Requirements
Must have
• Must follow company's logo color and style. Must have the company's log on its.

```html
<!DOCTYPE html>
<html lang="en">
<head>
<meta charset="utf-8">
<title>Velocrypt Business Card</title>
<link href="https://fonts.googleapis.com/css2?family=Lato:wght@400;700;900&display=swap" rel="stylesheet">
<style>
  :root {
    --page-bg: #d9d6d2;
    --card-bg: #f1f0ee;
    --ink: #1a1a1a;
    --swoosh: #111111;
    --accent-red: #8e1f24;
    --name-red: #9a2a2e;
    --soft-light: #e6e2de;
    --photo-dark: #3b3b3d;
    --photo-mid: #6d6a68;
    --photo-light: #9c9793;
  }
  * { margin: 0; padding: 0; box-sizing: border-box; }
  html, body {
    width: 1200px; height: 970px; overflow: hidden;
    background: var(--page-bg);
    font-family: "Lato", Arial, sans-serif;
  }
  .card {
    position: absolute; left: 100px; top: 207px;
    width: 1000px; height: 556px;
    background: var(--card-bg);
    overflow: hidden;
    box-shadow: 0 10px 30px rgba(0,0,0,0.18);
  }
  .card-art { position: absolute; inset: 0; width: 1000px; height: 556px; }
  .brand-name {
    position: absolute; right: 43px; top: 50px;
    font-weight: 900; font-size: 104px; line-height: 1;
    color: var(--ink); letter-spacing: -1px;
  }
  .address {
    position: absolute; right: 43px; top: 168px;
    text-align: right; font-size: 26px; line-height: 32px;
    color: var(--ink);
  }
  .holder { position: absolute; left: 39px; top: 280px; }
  .holder-name { font-weight: 700; font-size: 36px; color: var(--name-red); line-height: 42px; }
  .holder-title { font-size: 28px; color: var(--soft-light); line-height: 36px; }
  .contacts { position: absolute; left: 39px; top: 396px; list-style: none; }
  .contacts li {
    display: flex; align-items: center; gap: 12px;
    font-size: 24px; line-height: 33.5px; color: var(--soft-light);
  }
  .contacts svg { width: 24px; height: 24px; fill: var(--accent-red); flex: none; }
</style>
</head>
<body>
  <div class="card">
    <svg class="card-art" viewBox="0 0 1000 556" aria-hidden="false">
      <defs>
        <linearGradient id="photoTone" x1="0" y1="0" x2="1" y2="1">
          <stop offset="0" stop-color="var(--photo-dark)"/>
          <stop offset="0.5" stop-color="var(--photo-mid)"/>
          <stop offset="1" stop-color="var(--photo-light)"/>
        </linearGradient>
      </defs>
      <path role="img" aria-label="Photo of a padlock resting on a laptop keyboard"
            d="M0,238 Q520,215 985,556 L0,556 Z" fill="url(#photoTone)"/>
      <path class="red-line" d="M0,232 Q520,208 990,556" fill="none" stroke="var(--accent-red)" stroke-width="6"/>
      <path class="swoosh" d="M0,170 Q460,120 1000,556 Q500,190 0,222 Z" fill="var(--swoosh)"/>
    </svg>

    <div class="brand-name">velocrypt</div>
    <div class="address">0000 Harbor Lane<br>Brookfield, WI 00000-0000</div>

    <div class="holder">
      <div class="holder-name">Alan Brooks</div>
      <div class="holder-title">President</div>
    </div>

    <ul class="contacts">
      <li><svg viewBox="0 0 24 24"><path d="M3 9c0-3 4-5 9-5s9 2 9 5l-4 1-1-3H8L7 10 3 9zm3 2h12l2 9H4l2-9zm6 2a3 3 0 100 6 3 3 0 000-6z"/></svg>321 555 0148</li>
      <li><svg viewBox="0 0 24 24"><path d="M6 3h12v5H6zM3 9h18v8h-3v4H6v-4H3zm5 6v4h8v-4z"/></svg>854 555 0193</li>
      <li><svg viewBox="0 0 24 24"><path d="M2 5h20v14H2zm2 2v1l8 5 8-5V7l-8 5z"/></svg>info@velocrypt.com</li>
      <li><svg viewBox="0 0 24 24"><path d="M12 2a10 10 0 100 20 10 10 0 000-20zm-1 2.1V8H7.5A8 8 0 0111 4.1zm2 0A8 8 0 0116.5 8H13zM4.3 10H11v4H4.3a8 8 0 010-4zm8.7 0h6.7a8 8 0 010 4H13zm-5.5 6H11v3.9A8 8 0 017.5 16zm5.5 0h3.5a8 8 0 01-3.5 3.9z"/></svg>www.velocrypt.com</li>
    </ul>
  </div>
</body>
</html>
```